Young Accounting firm needing a captivating business card

We need a business card design that forces the person to look at the card because its either gold foil, plastic, or lettering pop up etc. We already have a logo with a specific gold color and we need to make it pop. We are an accounting firm. I need the words" accounting, payroll, licenses, audits, taxes" somewhere on the business card so as to describe what we do- preferably on the side where the logo is at.

Industry/Entity Type

Accounting

Contact Information for Business Card

Address 48276 9th Ave S Ste 305, Federal Way, WA 98117
Business Phone (360)418-2096
Fax (360)418-2157
Office Cell Phone (360)586-7319

Font styles to use
Serif

Colors
85abd2

Requirements
Must have
• It should state
• "Accounting" "Taxes" "Audits" "Licenses" "Payroll"
Nice to have
• Matte with gold foil, different textures, With Either a textured ivory background or gray blue slate background
Should not have
• colorful colors

```html
<!DOCTYPE html>
<html lang="en">
<head>
<meta charset="utf-8">
<title>Norvale Ledger — Business Card</title>
<link rel="stylesheet" href="https://fonts.googleapis.com/css2?family=Lato:wght@400;700&display=swap">
<style>
  :root {
    --backdrop: #2b2b2d;
    --card: #1b1b1c;
    --card-pattern: #161617;
    --gold: #c9a227;
    --silver: #c9c9c9;
    --white: #f4f4f4;
    --rule: #6a6a6a;
  }
  * { box-sizing: border-box; margin: 0; padding: 0; }
  html, body { width: 1200px; height: 1108px; overflow: hidden; }
  body {
    background: var(--backdrop);
    font-family: "Lato", sans-serif;
    position: relative;
  }
  .card {
    position: absolute;
    top: 259px;
    width: 360px;
    height: 590px;
    background: var(--card);
    border-radius: 22px;
    box-shadow: 0 18px 40px rgba(0,0,0,.55);
    overflow: hidden;
  }
  .card--front { left: 200px; }
  .card--back { left: 640px; }

  /* front */
  .brand {
    position: absolute;
    top: 130px; left: 0; right: 0;
    display: flex; align-items: center; justify-content: center; gap: 12px;
  }
  .brand__mark { width: 26px; height: 26px; background: var(--gold); }
  .brand__name {
    color: var(--gold);
    font-weight: 700;
    font-size: 36px;
    letter-spacing: .5px;
  }
  .person { position: absolute; top: 300px; left: 0; right: 0; text-align: center; }
  .person__name {
    color: var(--gold); font-weight: 700; font-size: 22px;
    letter-spacing: 1px; text-transform: uppercase;
  }
  .person__role { color: var(--silver); font-size: 17px; margin-top: 2px; }
  .contact-icons {
    position: absolute; top: 368px; left: 40px; right: 40px;
    display: flex; align-items: center; gap: 8px;
  }
  .contact-icons .rule { flex: 1; height: 1px; background: var(--rule); }
  .contact-icons svg { width: 22px; height: 22px; }
  .contact-list {
    position: absolute; top: 402px; left: 0; right: 0;
    text-align: center; color: var(--silver); font-size: 17px; line-height: 25px;
  }
  .address-rule {
    position: absolute; top: 510px; left: 40px; right: 40px;
    height: 1px; background: var(--rule);
  }
  .address {
    position: absolute; top: 520px; left: 0; right: 0;
    text-align: center; color: var(--silver); font-size: 17px; line-height: 24px;
  }

  /* back */
  .back-texture {
    position: absolute; inset: 0;
    background: radial-gradient(circle at 40% 30%, #1f1f20, var(--card-pattern));
  }
  .back-brand {
    position: absolute; top: 390px; left: 0; right: 0;
    display: flex; align-items: center; justify-content: center; gap: 10px;
  }
  .back-brand .brand__mark { width: 20px; height: 20px; }
  .back-brand .brand__name { font-size: 24px; }
  .services {
    position: absolute; top: 470px; left: 0; right: 0;
    text-align: center; color: var(--white);
    font-size: 19px; line-height: 28px; text-transform: uppercase; letter-spacing: .3px;
  }
</style>
</head>
<body>
  <section class="card card--front">
    <div class="brand">
      <span class="brand__mark"></span>
      <span class="brand__name">Norvale Ledger</span>
    </div>
    <div class="person">
      <p class="person__name">Dana Whitfield</p>
      <p class="person__role">Managing Director</p>
    </div>
    <div class="contact-icons">
      <span class="rule"></span>
      <svg viewBox="0 0 22 22" aria-label="Phone"><circle cx="11" cy="11" r="11" fill="var(--gold)"/><path d="M7 6c1 0 2 2 2 3s-1 1 0 2 2 2 2 2 1-1 2 0 3 1 3 2-1 2-2 2C10 17 5 12 5 8c0-1 1-2 2-2z" fill="var(--card)"/></svg>
      <svg viewBox="0 0 22 22" aria-label="Fax"><circle cx="11" cy="11" r="11" fill="var(--gold)"/><rect x="6" y="9" width="10" height="6" rx="1" fill="var(--card)"/><rect x="8" y="5" width="6" height="4" fill="var(--card)"/><rect x="8" y="14" width="6" height="3" fill="var(--card)"/></svg>
      <svg viewBox="0 0 22 22" aria-label="Mobile"><circle cx="11" cy="11" r="11" fill="var(--gold)"/><rect x="8" y="5" width="6" height="12" rx="1" fill="var(--card)"/></svg>
      <svg viewBox="0 0 22 22" aria-label="Email"><circle cx="11" cy="11" r="11" fill="var(--gold)"/><rect x="6" y="7" width="10" height="8" fill="var(--card)"/><path d="M6 7l5 4 5-4" stroke="var(--gold)" fill="none"/></svg>
      <span class="rule"></span>
    </div>
    <div class="contact-list">
      <p>(360)418-2096</p>
      <p>(360)418-2157</p>
      <p>(360)586-7319</p>
      <p>hello@norvaleledger.com</p>
    </div>
    <div class="address-rule"></div>
    <div class="address">
      <p>48276 9th Ave S Ste 305</p>
      <p>Federal Way, WA 98117</p>
    </div>
  </section>

  <section class="card card--back">
    <div class="back-texture" role="img" aria-label="Tone-on-tone repeating brand pattern"></div>
    <div class="back-brand">
      <span class="brand__mark"></span>
      <span class="brand__name">Norvale Ledger</span>
    </div>
    <div class="services">
      <p>Accounting • Taxes • Audits</p>
      <p>Licenses • Payroll</p>
    </div>
  </section>
</body>
</html>
```